Night Dresses business cards business requirers

We are a new company initiating Mexico operations. Our core business is Night woman dress (both formal and party dress) for rent. Gownhaven is the name of the company. ITS Gownhaven form by two word. The dress word and topia (Utopic) so the place Gownhaven Means That You cant get the ideal, perfect and unique dress for your event. So we would like a modern, very creative, and attractive business card.

Industry/Entity Type

Womens Clothing

Contact Information for Business Card

Rounded Borders, two faces

Requirements
Must have
• Rounded borders, logo and slogan, modern, glam, attractive design
Should not have
• modern design classic or not

```html
<!DOCTYPE html>
<html lang="en">
<head>
<meta charset="utf-8">
<title>Gownhaven Business Card</title>
<link rel="stylesheet" href="https://fonts.googleapis.com/css2?family=Open+Sans:ital,wght@0,400;0,600;1,400&display=swap">
<style>
  :root {
    --backdrop: #2b2b2d;
    --card-white: #ffffff;
    --plum: #a4547f;
    --plum-light: #b5669a;
    --plum-dark: #974a76;
    --swoosh-grey: #545456;
    --text-grey: #58585a;
    --white: #ffffff;
  }
  * { margin: 0; padding: 0; box-sizing: border-box; }
  html, body {
    width: 1200px; height: 999px; overflow: hidden;
    background: var(--backdrop);
    font-family: "Open Sans", Arial, sans-serif;
  }
  .canvas { position: relative; width: 1200px; height: 999px; }

  .card { position: absolute; border-radius: 40px; overflow: hidden; }

  /* Front card */
  .card-front { left: 97px; top: 22px; width: 800px; height: 458px; background: var(--card-white); }
  .card-front .waves { position: absolute; left: 0; top: 0; }
  .brand-name {
    position: absolute; left: 33px; top: 80px;
    font-size: 28px; font-weight: 600; letter-spacing: 5px; color: var(--text-grey);
    white-space: nowrap; line-height: 1;
  }
  .contact { position: absolute; left: 524px; top: 92px; color: var(--text-grey); }
  .contact .person-name { font-size: 32px; font-style: italic; line-height: 1; }
  .contact .designation { font-size: 17px; margin-top: 8px; }
  .contact .address { font-size: 17px; line-height: 22px; margin-top: 27px; }
  .contact .lines { list-style: none; margin-top: 24px; }
  .contact .lines li {
    display: flex; align-items: center; gap: 18px;
    font-size: 17px; height: 28px;
  }
  .contact .lines svg { width: 18px; height: 18px; flex: none; }
  .tagline {
    position: absolute; left: 44px; top: 404px;
    font-size: 18px; font-weight: 600; color: var(--white);
  }

  /* Back card */
  .card-back {
    left: 292px; top: 516px; width: 798px; height: 456px;
    background: radial-gradient(ellipse at 45% 45%, var(--plum-light) 0%, var(--plum) 55%, var(--plum-dark) 100%);
  }
  .brand-name-back {
    position: absolute; left: 0; width: 100%; top: 206px; text-align: center;
    font-size: 40px; font-weight: 600; letter-spacing: 10px; color: var(--white);
    padding-left: 10px; line-height: 1;
  }
</style>
</head>
<body>
<main class="canvas">

  <section class="card card-front">
    <svg class="waves" width="800" height="458" viewBox="0 0 800 458" aria-hidden="true">
      <defs>
        <linearGradient id="plumBand" x1="0" y1="0" x2="1" y2="0">
          <stop offset="0" stop-color="#a0527d"/>
          <stop offset="0.6" stop-color="#b0608f"/>
          <stop offset="1" stop-color="#9a4c78"/>
        </linearGradient>
      </defs>
      <path d="M0,245 C220,352 520,400 800,342 L800,368 C520,420 220,368 0,256 Z" fill="var(--swoosh-grey)"/>
      <path d="M0,264 C200,382 500,432 800,393 L800,458 L0,458 Z" fill="url(#plumBand)"/>
    </svg>

    <div class="brand-name">GOWNHAVEN</div>

    <div class="contact">
      <p class="person-name">Name Title</p>
      <p class="designation">designation</p>
      <p class="address">suit # 00, Lorem ipsum<br>Lorem Lorem ipsum</p>
      <ul class="lines">
        <li>
          <svg viewBox="0 0 18 18" aria-label="Phone"><rect x="1" y="1" width="16" height="16" rx="3" fill="var(--text-grey)"/><path d="M6,4 C5,6 6,11 11,14 L13,12 L11,10 L10,11 C8,10 7,8 7,7 L8,6 Z" fill="#fff"/></svg>
          000-000-0000
        </li>
        <li>
          <svg viewBox="0 0 18 18" aria-label="Fax"><rect x="5" y="1" width="8" height="6" fill="var(--text-grey)"/><rect x="2" y="8" width="14" height="6" rx="1" fill="var(--text-grey)"/><rect x="1" y="15" width="16" height="2" fill="var(--text-grey)"/></svg>
          000-000-0000
        </li>
        <li>
          <svg viewBox="0 0 18 18" aria-label="Email"><path d="M1,7 L9,2 L17,7 L17,16 L1,16 Z" fill="var(--text-grey)"/><path d="M3,8 L9,12 L15,8" stroke="#fff" stroke-width="1.5" fill="none"/></svg>
          abcd@mailbox.com
        </li>
      </ul>
    </div>

    <p class="tagline">modern, glam , attractive design</p>
  </section>

  <section class="card card-back">
    <div class="brand-name-back">GOWNHAVEN</div>
  </section>

</main>
</body>
</html>
```